A5 Patient Information Booklet (Chiropractic Clinic) 4-8 pages

Here’s a polished, professional rewrite of your full brief and content, with clearer structure, corrected language, and a premium tone:

---

**Project Title:** Premium Patient Information Brochure (Chiropractic & Wellness Clinic)

---

### **Overview**

We are a health and wellness clinic seeking a premium, high-end patient information brochure to provide following a patient’s initial consultation and first treatment.

The purpose of this booklet is to:

* Reinforce trust and professionalism
* Help patients understand what to expect next
* Encourage adherence to care recommendations
* Position the clinic as calm, expert-led, and results-driven

---

### **Format**

* 4–8 page booklet (A5 or similar size)
* Print-ready and digital versions required

---

### **Target Audience**

Patients who have just completed their initial consultation and may have begun treatment. They may already be experiencing physical or mental changes, so the brochure should guide, reassure, and educate them on what comes next.

---

### **Tone & Style**

* Premium, calm, and reassuring
* Modern wellness aesthetic (not overly clinical)
* Clean layout with minimal clutter
* Soft, neutral colour palette (whites, creams, muted greens, soft blues)
* Elegant typography (e.g. Montserrat / Lato)
* High-end, trustworthy, and professional feel

---

### **Key Messages**

#### 1. Listen to Your Body

Patients may feel different after treatment. Reassure them that this is normal and part of the healing process.

#### 2. Post-Treatment Advice

* Stay well hydrated
* Rest if needed
* Avoid overexertion if the body requires recovery

#### 3. Healing is a Journey (Core Concept)

A strong visual metaphor of a **“road to recovery”** or **journey** should be central to the design.

This journey should clearly illustrate three phases:

* **Phase 1: Initial Care (Weeks 1–6)**
Focus: Reducing pain/discomfort, calming the body, and initiating response to treatment

* **Phase 2: Corrective Care (Weeks 6–12)**
Focus: Addressing underlying issues, improving function, and creating lasting change

* **Phase 3: Wellness / Maintenance (Ongoing)**
Focus: Maintaining progress, preventing relapse, and supporting long-term wellbeing

**Important:**

* Emphasise that this is not a quick fix
* Progress requires time and consistency
* Each patient follows an individualised care plan
* The journey should feel structured, positive, and achievable

#### 4. Personalised Care

Reinforce that every treatment plan is tailored specifically to the individual.

#### 5. Professional Reassurance

Patients should feel confident they are in expert hands and supported throughout their journey.

---

### **Design Direction**

* Use imagery that reflects calmness, progression, and wellness (e.g. pathways, nature, soft gradients)
* Avoid generic stock imagery
* **Only use original clinic images from website and social media**
* Prioritise white space and clarity
* Aim for a luxury spa/medical hybrid aesthetic

---

## **Content Structure (Page-by-Page)**

### **Front Cover**

* Clean, minimal, premium design
* Clinic branding

---

### **Page 1: Patient Case Summary**

**Title:** *Welcome to Larkmoor Spine Studio*

Thank you for choosing Larkmoor Spine Studio.

This booklet is designed to guide you through:

* What we found during your initial consultation
* Your personalised recommended treatment plan
* Your road to recovery
* Long-term wellness care
* Why we take the approach we do

---

### **Page 2: Your Care Journey**

**Stage 1: Your Initial Consultation**

Today we completed a comprehensive assessment of your health and function, including:

* Full case history and discussion of your symptoms and goals
* Orthopaedic and neurological testing
* Postural and movement assessment
* Initial treatment (where appropriate)

**What this tells us:**

* How your body is currently functioning
* Where areas of stress or dysfunction may be present
* The most appropriate and effective path forward for your care

---

### **Page 3: Your Suggested Treatment Plan**

Based on today’s findings, your recommended care plan is:

**______ treatments over ______ weeks**

This should be viewed alongside your *Road to Recovery* to help you understand what to expect.

We have also discussed:

* Expected timelines for improvement
* Available payment options

**After Treatment:**
It is common to feel different following treatment. This is a normal response as your body begins to adapt and respond.

We recommend:

* Staying well hydrated
* Allowing time for rest and recovery
* Avoiding overexertion if your body feels it needs it

---

### **Page 4: What to Expect Next**

Healing is not always linear—it is a process that occurs over time.

Your care will typically progress through the following stages:

* **Relief Care**
Focused on reducing discomfort and calming the body

* **Corrective Care**
Focused on addressing underlying issues and improving function
(This phase may include prescribed exercises)

* **Maintenance / Wellness Care**
Focused on sustaining progress, preventing recurrence, and supporting long-term health

---

### **Page 5: Understanding Chiropractic Care**

**What is Chiropractic?**
Chiropractic care focuses on the relationship between the spine, nervous system, and overall body function.

By improving spinal movement and alignment, chiropractic care helps support the nervous system, allowing the body to function and heal more effectively.

**About Larkmoor Spine Studio**
At Larkmoor Spine Studio, our approach is centred around personalised, patient-focused care. We aim to not only relieve symptoms but to address underlying causes and support long-term wellbeing.

---

### **Back Page**

* Clinic contact details
* Website
* Social media icons/handles

**Closing Message:**
“A healthier, stronger you—supported every step of the way.”

---

### **Deliverables**

* Print-ready PDF
* Editable source files

---

### **Additional Notes**

* The brochure should feel valuable and worth keeping
* Encourage long-term care in a subtle, non-pushy way
* Maintain clarity, readability, and strong visual hierarchy
* Balance professionalism with warmth and approachability

---

If you’d like, I can also turn this into **actual brochure copy (fully written, patient-facing text)** or help you refine it further for a designer.

Target Market(s)

Existing patients who want to feel better and look after themselves that is given after their initil consultation appointment

Industry/Entity Type

Chiropractic, wellness, health

Font styles to use
Other font styles liked:
• Montserrat or Lato

Colors
0094D4
00A9DD
6FCCEA
C7EBF8
E9F6FB
00AB8E
00BBA5
67D7C9
C6EFE9
E9F9F6
6B429C
8869AF
B7A5CE
E3DAEB
F3F0F8

Requirements
Must have
• my own photos, look premium wellness, be clear and simple to understand for patients journey or what to expect next and over time
Nice to have
• USe my social media/website for ideas
Should not have
• generic photos and images

```html
<!DOCTYPE html>
<html lang="en">
<head>
<meta charset="utf-8">
<title>Larkmoor Spine Studio – Patient Booklet</title>
<link rel="stylesheet" href="https://fonts.googleapis.com/css2?family=Playfair+Display:wght@400;500&family=Montserrat:ital,wght@0,400;0,500;0,600;0,700;1,400;1,600&family=Allura&display=swap">
<style>
:root{
  --stage:#3d4350;
  --paper:#ffffff;
  --ink:#2f5555;
  --ink-dark:#262a2e;
  --body:#2d3436;
  --teal:#00ab8e;
  --teal-mid:#14a39a;
  --teal-deep:#2e6b6b;
  --teal-soft:#e3f7f4;
  --purple:#8869af;
  --blue:#4b8bb5;
  --lavender:#e3daeb;
  --rule:#5fb9b0;
}
*{margin:0;padding:0;box-sizing:border-box}
html,body{width:1200px;height:2286px;overflow:hidden;background:var(--stage)}
body{position:relative;font-family:'Montserrat',sans-serif;color:var(--body)}
.page{position:absolute;width:480px;height:682px;background:var(--paper);overflow:hidden}
.p-cover{left:114px;top:108px}
.p-expect{left:606px;top:108px}
.p-journey{left:114px;top:803px}
.p-plan{left:606px;top:803px}
.p-contact{left:114px;top:1497px}
.p-back{left:606px;top:1497px}
.abs{position:absolute}
.center{left:0;right:0;text-align:center}
.serif{font-family:'Playfair Display',serif;color:var(--ink);font-weight:400}
.script{font-family:'Allura',cursive}
.rule{position:absolute;height:1px;background:var(--rule)}
.photo{position:absolute}
/* cover */
.cover-photo{inset:0;background:linear-gradient(180deg,#ece8e3 0%,#e4d4bd 40%,#d7b68c 75%,#c59a68 100%)}
.brand-mark{position:absolute;border-radius:50%;border:3px solid #79a6d6}
.brand-name{position:absolute;font-family:'Playfair Display',serif;font-weight:500;color:var(--ink-dark);text-align:center;letter-spacing:.3px}
.cover-title{top:176px;font-size:37px;line-height:38px}
.cover-script{top:244px;font-size:46px;line-height:52px;color:var(--ink)}
.cover-sub{top:309px;font-size:13px;line-height:16px;color:var(--ink)}
.cover-sign{left:37px;top:585px;font-size:34px;line-height:30px;color:#fff}
/* headings */
.h-title{top:42px;font-size:27px;line-height:31px}
.h-big{font-size:44px;line-height:44px}
.h-small{font-size:26px;line-height:28px}
.sub{font-size:12.5px;font-weight:600;color:var(--teal-deep);line-height:18px}
/* expect */
.sec-title{font-size:18.5px;font-weight:500;color:var(--teal-deep)}
.txt{font-size:11.5px;line-height:17.5px;color:var(--body)}
.accent{color:var(--teal);font-weight:600}
.ticks{list-style:none}
.ticks li{position:relative;padding-left:19px;font-size:11.5px;line-height:17px;margin-bottom:6px}
.ticks li::before{content:"";position:absolute;left:0;top:3px;width:11px;height:11px;border-radius:50%;background:var(--teal)}
.ticks li::after{content:"";position:absolute;left:3px;top:5px;width:5px;height:3px;border-left:1.5px solid #fff;border-bottom:1.5px solid #fff;transform:rotate(-45deg)}
.dot{position:absolute;border-radius:50%;display:flex;align-items:center;justify-content:center}
.dot-dark{background:var(--teal-deep)}
.dot-teal{background:var(--teal)}
.tip{font-size:11.5px;line-height:17.5px}
.expect-photo{left:0;top:404px;width:180px;height:278px;background:linear-gradient(90deg,#b8a590 0%,#d8cbbd 45%,rgba(255,255,255,0) 100%)}
.note-box{left:122px;top:602px;width:272px;height:37px;background:var(--teal-soft)}
/* journey */
.road{left:0;top:300px;width:240px;height:290px;border-top-right-radius:100% 100%;background:linear-gradient(180deg,rgba(198,239,233,.15) 0%,#c3e8e2 35%,#d6c8ea 78%,#efe6f6 100%)}
.phase{position:absolute}
.phase-num{font-size:16px;font-weight:600;line-height:18px}
.phase-name{font-size:10px;font-weight:500;line-height:14px}
.pill{display:inline-block;font-size:8.5px;font-weight:700;color:#fff;letter-spacing:.6px;border-radius:8px;padding:1px 12px;margin:2px 0 3px}
.bullets{list-style:none}
.bullets li{position:relative;padding-left:9px;font-size:9.8px;line-height:14.5px}
.bullets li::before{content:"•";position:absolute;left:0;color:var(--teal)}
.stem{position:absolute;width:1px}
.journey-note{left:37px;top:586px;width:420px;font-size:11.5px;line-height:17.5px;background:#fff}
/* plan */
.form{left:40px;top:202px;width:411px;height:143px;border:1.4px solid var(--rule);border-radius:7px}
.form-label{position:absolute;font-size:8.5px;font-weight:600;color:var(--ink-dark)}
.form-line{position:absolute;height:1.4px;background:var(--rule)}
.plan-note{top:357px;font-size:12px;line-height:18px;font-style:italic;font-weight:600;color:var(--teal-deep)}
.pillar{position:absolute;width:128px;text-align:center;top:447px}
.pillar-title{font-size:11.8px;font-weight:600;color:var(--teal-mid);line-height:18px}
.pillar-rule{width:64px;height:1px;background:#cfe4e1;margin:5px auto 5px}
.pillar-text{font-size:8.3px;line-height:12.5px;color:#555}
.plan-photo{left:0;top:522px;width:480px;height:160px;background:linear-gradient(180deg,rgba(255,255,255,1) 0%,#b5b5b5 30%,#6e6e6e 70%,#8a8a8a 100%)}
.plan-sign{left:0;right:0;top:612px;text-align:center;font-size:31px;color:#fff}
/* contact */
.contact-row{position:absolute;left:133px;font-size:17.5px;line-height:25.5px;color:#3a5555}
.c-icon{position:absolute;left:90px}
.follow{top:462px;font-size:40px;color:var(--ink)}
.social{position:absolute;top:527px;width:20px;height:20px;border-radius:50%;border:2px solid var(--teal)}
.band{left:0;top:588px;width:480px;height:94px;background:var(--teal-soft)}
.band-text{top:625px;font-size:17.5px;font-style:italic;color:var(--teal-deep)}
/* back */
.back-photo{inset:0;background:linear-gradient(160deg,#f3e7cf 0%,#e8cfa3 35%,#dab27d 65%,#c59a6c 100%)}
</style>
</head>
<body>

<!-- Front cover -->
<section class="page p-cover">
  <div class="photo cover-photo" role="img" aria-label="Photo of a chiropractor's hands treating a patient lying face down on a treatment table in warm light"></div>
  <div class="brand-mark" style="left:192px;top:29px;width:96px;height:96px"></div>
  <div class="brand-name center" style="top:130px;font-size:19px">Larkmoor Spine Studio</div>
  <h1 class="abs center serif cover-title">Your Journey to<br>Better Health</h1>
  <div class="abs center script cover-script">Starts Here</div>
  <div class="rule" style="left:132px;width:216px;top:301px;background:var(--ink)"></div>
  <p class="abs center cover-sub">Chiropractic &amp; Wellness Care,<br>Tailored to You</p>
  <p class="abs script cover-sign">You're in the<br>right place.</p>
</section>

<!-- What to expect -->
<section class="page p-expect">
  <h2 class="abs center serif h-title" style="top:42px;font-size:26px">What to Expect<br>After Your Treatment</h2>
  <div class="rule" style="left:120px;width:239px;top:130px"></div>
  <h3 class="abs sec-title" style="left:178px;top:154px">1. Listen to Your Body</h3>
  <p class="abs txt" style="left:178px;top:182px;width:260px">After your treatment, it's normal<br>to feel different.<br>Your body is beginning to respond,<br>adapt, and heal.</p>
  <p class="abs txt accent" style="left:178px;top:254px">You may notice:</p>
  <ul class="abs ticks" style="left:178px;top:276px;width:240px">
    <li>Mild soreness or stiffness</li>
    <li>Increased awareness in<br>certain areas</li>
    <li>A sense of release or fatigue</li>
  </ul>
  <p class="abs txt" style="left:178px;top:360px">This is all part of the process.</p>
  <div class="rule" style="left:120px;width:239px;top:409px"></div>

  <div class="photo expect-photo" role="img" aria-label="Photo of a chiropractor smiling while assessing a seated patient's back"></div>
  <div class="dot dot-dark" style="left:120px;top:446px;width:40px;height:40px">
    <svg width="14" height="18" viewBox="0 0 14 18"><path d="M7 1C4 6 1 9 1 12a6 6 0 0 0 12 0c0-3-3-6-6-11z" fill="#fff"/></svg>
  </div>
  <h3 class="abs sec-title" style="left:178px;top:441px">2. Support Your Recovery</h3>
  <div class="dot dot-teal" style="left:178px;top:478px;width:22px;height:22px"><svg width="10" height="12" viewBox="0 0 10 12"><path d="M1 1h8l-1 10H2z" fill="#fff"/></svg></div>
  <p class="abs tip" style="left:208px;top:481px">Stay well hydrated</p>
  <div class="dot dot-teal" style="left:178px;top:513px;width:22px;height:22px"><svg width="12" height="8" viewBox="0 0 12 8"><rect x="0" y="3" width="12" height="3" fill="#fff"/><rect x="0" y="0" width="2" height="8" fill="#fff"/></svg></div>
  <p class="abs tip" style="left:208px;top:516px">Allow your body time to rest</p>
  <div class="dot dot-teal" style="left:178px;top:549px;width:22px;height:22px"><svg width="12" height="12" viewBox="0 0 12 12"><circle cx="6" cy="2" r="1.6" fill="#fff"/><path d="M1 4l5 1 5-1M6 5v3l-3 4M6 8l3 4" stroke="#fff" stroke-width="1.4" fill="none"/></svg></div>
  <p class="abs tip" style="left:208px;top:552px;width:240px">Avoid overexertion if you feel you<br>need recovery</p>
  <div class="abs note-box"></div>
  <div class="dot dot-dark" style="left:120px;top:600px;width:40px;height:40px"><svg width="16" height="16" viewBox="0 0 16 16"><path d="M8 15V8M8 8C8 4 5 2 2 2c0 4 3 6 6 6zM8 10c0-3 3-5 6-5 0 3-3 5-6 5z" fill="#fff"/></svg></div>
  <p class="abs tip" style="left:176px;top:603px;width:220px">Your body knows how to heal —we're<br>here to guide it.</p>
</section>

<!-- Recovery journey -->
<section class="page p-journey">
  <h2 class="abs center serif h-small" style="top:42px">Your Recovery</h2>
  <div class="abs center serif h-big" style="top:68px">Journey</div>
  <div class="rule" style="left:71px;width:337px;top:129px"></div>
  <p class="abs center sub" style="top:151px">Healing is a process — structured, personal, and progressive.</p>
  <div class="abs road" role="img" aria-label="Illustration of a winding road fading from teal into lavender, symbolising the road to recovery"></div>

  <div class="stem" style="left:92px;top:208px;height:84px;background:var(--teal)"></div>
  <div class="dot" style="left:72px;top:188px;width:40px;height:40px;background:var(--teal)"><svg width="18" height="16" viewBox="0 0 18 16"><path d="M9 15V7M9 7C9 4 6 2 2 2c0 3 3 5 7 5zM9 7c0-3 3-5 7-5 0 3-3 5-7 5zM3 15h12" stroke="#fff" stroke-width="1.4" fill="none"/></svg></div>
  <div class="phase" style="left:123px;top:188px;color:var(--teal)">
    <div class="phase-num">PHASE 1</div>
    <div class="phase-name">Initial Care</div>
    <span class="pill" style="background:var(--teal)">WEEKS 1–6</span>
    <ul class="bullets" style="color:var(--body)"><li>Reducing pain and discomfort</li><li>Calming the nervous system</li><li>Helping your body begin<br>to respond</li></ul>
  </div>

  <div class="stem" style="left:243px;top:331px;height:95px;background:var(--purple)"></div>
  <div class="dot" style="left:223px;top:311px;width:40px;height:40px;background:var(--purple)"><svg width="18" height="14" viewBox="0 0 18 14"><path d="M1 13L7 3l3 5 2-3 5 8z" fill="#fff"/></svg></div>
  <div class="phase" style="left:273px;top:306px;color:var(--purple)">
    <div class="phase-num">PHASE 2</div>
    <div class="phase-name">Corrective Care</div>
    <span class="pill" style="background:var(--purple)">WEEKS 6–12</span>
    <ul class="bullets" style="color:var(--body)"><li>Addressing underlying issues</li><li>Improving movement<br>and function</li><li>Creating lasting structural<br>change</li></ul>
  </div>

  <div class="stem" style="left:243px;top:468px;height:86px;background:var(--blue)"></div>
  <div class="dot" style="left:223px;top:448px;width:40px;height:40px;background:var(--blue)"><svg width="16" height="18" viewBox="0 0 16 18"><circle cx="8" cy="3" r="2" fill="#fff"/><path d="M2 5l6 2 6-2M8 7v5l-2 5M8 12l2 5" stroke="#fff" stroke-width="1.6" fill="none"/></svg></div>
  <div class="phase" style="left:273px;top:444px;color:var(--blue)">
    <div class="phase-num">PHASE 3</div>
    <div class="phase-name">Wellness / Maintenance</div>
    <span class="pill" style="background:var(--teal-deep)">ONGOING</span>
    <ul class="bullets" style="color:var(--body)"><li>Maintaining progress</li><li>Preventing relapse</li><li>Supporting overall<br>wellbeing</li></ul>
  </div>

  <div class="abs journey-note">
    <p>This is not a quick fix.</p>
    <p>True healing takes consistency, time, and the right guidance.</p>
    <p style="font-style:italic;margin-top:7px">Every journey is different — your care plan is tailored specifically to you.</p>
  </div>
</section>

<!-- Care plan -->
<section class="page p-plan">
  <h2 class="abs center serif h-small" style="top:42px">Your Personalised</h2>
  <div class="abs center serif h-big" style="top:68px">Care Plan</div>
  <div class="rule" style="left:71px;width:337px;top:129px"></div>
  <p class="abs center sub" style="top:150px">Designed specifically for your body,<br>your goals, and your lifestyle</p>
  <div class="abs form">
    <span class="form-label" style="left:14px;top:12px">Patient Name:</span>
    <div class="form-line" style="left:0;right:0;top:35px"></div>
    <span class="form-label" style="left:14px;top:47px">Your Suggested Care Plan:</span>
    <div class="form-line" style="left:0;width:303px;top:71px"></div>
    <span class="form-label" style="left:324px;top:84px">treatments over</span>
    <div class="form-line" style="left:0;width:303px;top:107px"></div>
    <span class="form-label" style="left:324px;top:120px">weeks</span>
  </div>
  <p class="abs center plan-note">We'll guide you every step of the way,<br>adjusting your plan as your body progresses.</p>

  <div class="dot dot-teal" style="left:91px;top:405px;width:40px;height:40px"><svg width="14" height="18" viewBox="0 0 14 18"><circle cx="7" cy="4" r="3.5" fill="#fff"/><path d="M1 17v-5a6 6 0 0 1 12 0v5z" fill="#fff"/></svg></div>
  <div class="dot dot-teal" style="left:219px;top:405px;width:40px;height:40px"><svg width="16" height="18" viewBox="0 0 16 18"><path d="M8 1l7 3v5c0 4-3 7-7 8-4-1-7-4-7-8V4z" fill="#fff"/><path d="M4.5 9l2.5 2.5 4.5-5" stroke="#00ab8e" stroke-width="1.8" fill="none"/></svg></div>
  <div class="dot dot-teal" style="left:347px;top:405px;width:40px;height:40px"><svg width="18" height="16" viewBox="0 0 18 16"><path d="M9 8C7 5 3 5 3 8c0 2 3 4 6 6 3-2 6-4 6-6 0-3-4-3-6 0z" fill="#fff"/></svg></div>
  <div class="pillar" style="left:47px"><div class="pillar-title">Personalised<br>Approach</div><div class="pillar-rule"></div><div class="pillar-text">Care that's<br>tailored to you</div></div>
  <div class="pillar" style="left:175px"><div class="pillar-title">Evidence-Informed<br>Care</div><div class="pillar-rule"></div><div class="pillar-text">Safe, effective,<br>and professional</div></div>
  <div class="pillar" style="left:303px"><div class="pillar-title">Ongoing<br>Support</div><div class="pillar-rule"></div><div class="pillar-text">We're with you<br>for the long term</div></div>
  <div class="photo plan-photo" role="img" aria-label="Black and white photo of a chiropractor treating a patient's upper back"></div>
  <p class="abs script plan-sign">You. Stronger. Healthier. Happier.</p>
</section>

<!-- Contact -->
<section class="page p-contact">
  <h2 class="abs center serif h-title" style="top:42px;font-size:27px">We're Here for You<br>Every Step of the Way</h2>
  <div class="rule" style="left:120px;width:239px;top:130px"></div>
  <svg class="c-icon" style="top:187px" width="18" height="24" viewBox="0 0 18 24"><path d="M9 1a8 8 0 0 0-8 8c0 6 8 14 8 14s8-8 8-14a8 8 0 0 0-8-8z" fill="#00ab8e"/><circle cx="9" cy="9" r="3" fill="#fff"/></svg>
  <address class="contact-row" style="top:184px;font-style:normal">Larkmoor Spine Studio<br>Chiropractic &amp; Wellness<br>12 Fennick Row, Ashcombe<br>AC4 7JP</address>
  <svg class="c-icon" style="top:309px" width="22" height="22" viewBox="0 0 22 22"><path d="M5 2l4 4-2 3c1 3 3 5 6 6l3-2 4 4-3 3C9 20 2 13 2 5z" fill="#00ab8e"/></svg>
  <p class="contact-row" style="top:306px;font-weight:600">07700 900418</p>
  <svg class="c-icon" style="top:362px" width="20" height="15" viewBox="0 0 20 15"><rect x="0" y="0" width="20" height="15" rx="1.5" fill="#00ab8e"/><path d="M1 1l9 7 9-7" stroke="#fff" stroke-width="1.6" fill="none"/></svg>
  <p class="contact-row" style="top:355px">hello@larkmoorspine.co.uk</p>
  <svg class="c-icon" style="top:406px" width="20" height="20" viewBox="0 0 20 20"><circle cx="10" cy="10" r="8.5" stroke="#00ab8e" stroke-width="2" fill="none"/><ellipse cx="10" cy="10" rx="3.5" ry="8.5" stroke="#00ab8e" stroke-width="1.6" fill="none"/><path d="M2 10h16" stroke="#00ab8e" stroke-width="1.6"/></svg>
  <p class="contact-row" style="top:402px">www.larkmoorspine.co.uk</p>
  <p class="abs center script follow">Follow Us</p>
  <span class="social" style="left:207px" aria-label="Social profile"></span>
  <span class="social" style="left:247px" aria-label="Social profile"></span>
  <div class="abs band"></div>
  <p class="abs center band-text">Feel better. Move better. Live better. — Naturally.</p>
</section>

<!-- Back cover -->
<section class="page p-back">
  <div class="photo back-photo" role="img" aria-label="Photo of a chiropractor placing her hands on the upper back of a seated patient in soft golden light"></div>
  <div class="brand-mark" style="left:263px;top:49px;width:96px;height:96px"></div>
  <div class="brand-name" style="left:131px;width:360px;top:152px;font-size:19px">Larkmoor Spine Studio</div>
</section>

</body>
</html>
```